Cloud Software Services Business Needs New Website Design

Our client is looking for a really modern design for their cloud services company. We have a logo, but apart from that, if you read the brief fully and digest the wireframes, we hope you will come up with a really amazing end product.

The design of the website should be professional and trustworthy, it is there to inspire confidence in the services and softwares, as well as emphasising the track record of RMV and relative knowledge and competencies.

Given all the cloud-related communications in the messaging on the site, we will need this in either the imagery or icons in the site so that we can connect the messaging with the service offering.

The brand, being black, gives full range for the designer to present a palette that serves the brand, not forgetting the audience are generally IT decision-makers.

Target Market(s)

Managers and Directors Responsible for IT/Cloud Infrastructure

Industry/Entity Type

IT Technology

Number of Pages Required

5+ page

Font styles to use
Sans Serif

Requirements
Must have
• Initial designs which match the brief and wireframes, focus on the homepage and the winning designer will need to supply the internal pages for the website.
Nice to have
• Clearly considered professional website designs, with consistent design work and branding. If choosing stock imagery, then from PixHarbor Basics please.
Should not have
• Not too much colour, or too consumer/youthful.

```html
<!DOCTYPE html>
<html lang="en">
<head>
<meta charset="utf-8">
<title>RMV – Cloud Services</title>
<link href="https://fonts.googleapis.com/css2?family=Fira+Sans:wght@300;400;500;600;700&family=Hind:wght@400;500;600&display=swap" rel="stylesheet">
<style>
:root{
  --navy:#221b5e;
  --navy-deep:#16123f;
  --ink:#1d1b32;
  --text:#4a4a5c;
  --purple:#5a3cf0;
  --violet:#7b4cf6;
  --blue:#2f8ff2;
  --grey:#ededf3;
  --footer:#1c1b2b;
  --footer-text:#a9a9bd;
  --white:#ffffff;
}
*{margin:0;padding:0;box-sizing:border-box}
html,body{width:1200px;height:5246px;overflow:hidden}
body{font-family:"Hind",sans-serif;color:var(--text);background:var(--white);position:relative}
h1,h2,h3,.display{font-family:"Fira Sans",sans-serif;color:var(--ink)}
.abs{position:absolute}
.btn{position:absolute;display:flex;align-items:center;justify-content:center;border-radius:24px;font-family:"Fira Sans",sans-serif;font-weight:600;font-size:14px;letter-spacing:.8px;text-transform:uppercase;color:var(--white);text-decoration:none}
.btn-fill{background:linear-gradient(90deg,var(--blue),var(--purple))}
.btn-line{border:2px solid var(--white)}
/* top bar */
.topbar{position:absolute;left:0;top:0;width:1200px;height:51px;background:#1c1b2b;display:flex;justify-content:flex-end;gap:42px;padding:17px 98px 0 0;font-size:15px;color:#d9d9e6}
/* hero */
.hero{position:absolute;left:0;top:51px;width:1200px;height:760px;overflow:hidden}
.brand{position:absolute;left:100px;top:66px;font-family:"Fira Sans",sans-serif;font-weight:500;font-size:52px;color:var(--white);letter-spacing:2px}
.mainnav{position:absolute;top:28px;left:660px;display:flex;gap:34px;font-family:"Fira Sans",sans-serif;font-weight:500;font-size:18px;color:var(--white)}
.mainnav span::after{content:"";display:inline-block;width:6px;height:6px;border-right:2px solid #fff;border-bottom:2px solid #fff;transform:rotate(45deg);margin:0 0 4px 7px}
.hero-kicker{position:absolute;left:104px;top:278px;font-family:"Fira Sans",sans-serif;font-weight:300;font-size:36px;color:var(--white)}
.hero-title{position:absolute;left:104px;top:327px;font-weight:600;font-size:62px;color:var(--white)}
.hero-art{position:absolute;left:630px;top:72px;width:480px;height:550px;border-radius:40px;background:radial-gradient(circle at 55% 40%,#9b6cff 0,#5a3cf0 40%,rgba(34,27,94,0) 72%)}
.lining{position:absolute;left:0;width:1200px;top:602px;text-align:center;font-weight:600;font-size:38px;color:var(--white)}
.cards{position:absolute;top:729px;left:100px;display:flex;gap:26px}
.card{width:316px;height:159px;border-radius:8px;background:linear-gradient(135deg,var(--blue),var(--violet));box-shadow:0 10px 20px rgba(60,40,180,.25);display:flex;flex-direction:column;align-items:center;padding-top:20px}
.card .ico{width:56px;height:62px;border-radius:12px;background:linear-gradient(160deg,#ffd35a,#ff7a6a)}
.card p{margin-top:16px;font-family:"Fira Sans",sans-serif;font-size:26px;color:var(--white)}
/* intro */
.kicker{font-family:"Fira Sans",sans-serif;font-size:22px;color:var(--ink);font-weight:400}
.h-sec{font-weight:600;font-size:40px;color:var(--ink);line-height:1.15}
.copy{font-size:15.5px;line-height:25px;color:var(--text)}
.intro-copy{position:absolute;left:100px;top:1096px;width:520px}
.intro-copy p{margin-bottom:10px}
.intro-copy strong{color:var(--ink);font-weight:600}
.promise{display:flex;gap:8px;margin-bottom:12px}
.promise i{flex:none;width:22px;height:22px;border-radius:50%;background:linear-gradient(135deg,var(--blue),var(--purple));color:#fff;font-style:normal;font-size:11px;display:flex;align-items:center;justify-content:center;margin-top:1px}
.intro-frame{position:absolute;left:680px;top:985px;width:444px;height:529px;border-top:12px solid var(--purple);border-right:12px solid var(--purple);border-radius:0 16px 0 0}
.intro-photo{position:absolute;left:658px;top:1010px;width:444px;height:528px;border-radius:16px;background:radial-gradient(circle at 50% 40%,#3fb7ff 0,#1c4aa8 35%,#0d1640 75%)}
/* bands */
.band{position:absolute;left:0;width:1200px;background:linear-gradient(90deg,#3e6bd9 0%,#5a3cf0 55%,#6a3ff2 100%);text-align:center;color:var(--white)}
.band h2{color:var(--white);font-weight:300;font-size:42px}
.band h2 b{font-weight:600}
/* clouds carousel */
.provider{position:absolute;top:2226px;width:226px;height:220px}
.provider .box{position:absolute;left:0;top:8px;width:218px;height:212px;background:#4a3cc8;display:flex;flex-direction:column;align-items:center;padding-top:40px}
.provider .edge{position:absolute;left:12px;top:0;width:226px;height:212px;border-top:3px solid var(--blue);border-right:3px dashed var(--purple)}
.provider .name{font-family:"Fira Sans",sans-serif;font-weight:600;font-size:34px;color:var(--white);height:74px}
.provider .view{width:142px;height:40px;border:2px solid #fff;border-radius:22px;color:#fff;font-family:"Fira Sans",sans-serif;font-weight:600;font-size:14px;letter-spacing:.8px;display:flex;align-items:center;justify-content:center}
/* advice */
.advice{position:absolute;left:0;top:2552px;width:1200px;height:1025px;background:var(--grey)}
.ring{position:absolute;left:165px;top:3168px;width:334px;height:334px;border-radius:50%;background:linear-gradient(135deg,var(--blue),var(--purple));display:flex;align-items:center;justify-content:center}
.ring-inner{width:290px;height:290px;border-radius:50%;background:var(--grey);display:flex;flex-direction:column;align-items:center;justify-content:center;color:var(--purple);font-family:"Fira Sans",sans-serif}
/* blog */
.post{position:absolute;top:4003px;width:231px;height:383px;background:#fff;box-shadow:0 4px 14px rgba(30,30,60,.12)}
.post .img{height:163px}
.post .date{display:inline-block;margin:8px 0 0 16px;padding:2px 10px;border-radius:10px;background:linear-gradient(90deg,var(--blue),var(--purple));color:#fff;font-size:12px}
.post h3{font-size:19px;font-weight:600;line-height:22px;margin:6px 16px 0}
.post p{font-size:14.5px;line-height:21px;margin:8px 16px 0}
.post .btn{left:16px;top:332px;width:140px;height:42px}
/* trusted */
.trust{position:absolute;top:4590px;display:flex;flex-direction:column;align-items:center;width:150px}
.trust .mark{width:112px;height:80px;border-radius:40px;background:linear-gradient(135deg,var(--blue),var(--violet))}
.trust b{margin-top:12px;font-family:"Fira Sans",sans-serif;font-weight:600;font-size:16px;color:var(--ink);letter-spacing:1px}
/* footer */
.footer{position:absolute;left:0;top:4756px;width:1200px;height:490px;background:var(--footer)}
.fcol{position:absolute;top:98px;font-size:15px;line-height:33px;color:var(--footer-text)}
.fcol h4{font-family:"Fira Sans",sans-serif;font-weight:600;font-size:17px;color:var(--blue);margin-bottom:6px;letter-spacing:.3px}
.fcol svg{vertical-align:-2px;margin-right:6px}
.fbottom{position:absolute;left:100px;right:98px;top:440px;display:flex;font-size:14px;color:var(--footer-text)}
.fbottom nav{margin-left:auto;display:flex;gap:30px}
</style>
</head>
<body>

<div class="topbar"><span>Blog</span><span>Partners</span><span>About Us</span><span>Contact Us</span></div>

<header class="hero">
  <svg class="abs" style="left:0;top:0" width="1200" height="760" viewBox="0 0 1200 760" aria-hidden="true">
    <defs><linearGradient id="heroBg" x1="0" y1="0" x2="1" y2="1"><stop offset="0" stop-color="#2a2170"/><stop offset="1" stop-color="#1a154a"/></linearGradient></defs>
    <rect width="1200" height="760" fill="url(#heroBg)"/>
    <path d="M0 520 C 180 600 340 690 560 760 L0 760 Z" fill="#fff"/>
  </svg>
  <div class="brand">rmv</div>
  <nav class="mainnav"><span>Home</span><span>Cloud</span><span>Services</span><span>Software</span></nav>
  <div class="hero-kicker">Operatin</div>
  <h1 class="hero-title">Under A Cloud?</h1>
  <div class="hero-art" role="img" aria-label="Illustration of purple clouds above servers, a laptop and a phone"></div>
  <h2 class="lining">There’s Silver Lining</h2>
</header>

<div class="cards">
  <div class="card"><div class="ico" role="img" aria-label="Coin with downward arrow icon"></div><p>Reducing Costs</p></div>
  <div class="card"><div class="ico" role="img" aria-label="Documents moving icon"></div><p>Migration</p></div>
  <div class="card"><div class="ico" role="img" aria-label="Person with idea icon"></div><p>Work With Us</p></div>
</div>

<section>
  <div class="abs kicker" style="left:100px;top:1004px">Did the promise of cloud</div>
  <h2 class="abs h-sec" style="left:100px;top:1038px">Computing Hapen For You?</h2>
  <div class="intro-copy copy">
    <p>We didn’t think so! You’re not alone. There are many companies just like you who believed in the promise of cloud computing but are now shackled by it.</p>
    <p>But there is a silver lining, which is that RMV have built a business around helping companies improve their cloud efficiencies, reduce costs and simplify their operations as a result.</p>
    <p><strong>It can be summarised in three promises RMV makes to every client or partner:</strong></p>
    <div class="promise"><i>01</i><span>You can reduce cloud costs, without needing to move supplier</span></div>
    <div class="promise"><i>02</i><span>You can migrate from one cloud to another more easily</span></div>
    <div class="promise"><i>03</i><span>You can simp.N. your cloud management and choose your favoured provider</span></div>
    <p style="margin-top:18px">If you already know or want to talk to us just <strong>call 01632 960 481</strong><br><strong>or</strong></p>
  </div>
  <a class="btn btn-fill" style="left:100px;top:1556px;width:170px;height:45px">Send an email</a>
  <div class="intro-frame"></div>
  <div class="intro-photo" role="img" aria-label="Photo of a hand holding a tablet with a glowing cloud upload icon"></div>
</section>

<section class="band" style="top:1680px;height:349px">
  <h2 style="margin-top:75px">Your Cloud, <b>Your Tools</b></h2>
  <p class="display" style="color:#fff;font-size:26px;line-height:42px;margin-top:8px;font-weight:500">A Suite Of Software to Simplify<br>Deployment</p>
  <a class="btn btn-line" style="left:506px;top:237px;width:188px;height:45px">Cloud software</a>
</section>

<section>
  <div class="abs kicker" style="left:0;width:1200px;text-align:center;top:2104px">How hard is IT</div>
  <h2 class="abs h-sec" style="left:0;width:1200px;text-align:center;top:2138px">To moveyour Cloud?</h2>
  <svg class="abs" style="left:96px;top:2288px" width="36" height="60" aria-hidden="true"><path d="M30 4 L6 30 L30 56" fill="none" stroke="#1d1b32" stroke-width="3"/></svg>
  <svg class="abs" style="left:1068px;top:2288px" width="36" height="60" aria-hidden="true"><path d="M6 4 L30 30 L6 56" fill="none" stroke="#1d1b32" stroke-width="3"/></svg>
  <div class="provider" style="left:185px"><div class="edge"></div><div class="box"><div class="name">Stratobase</div><div class="view">View more</div></div></div>
  <div class="provider" style="left:485px"><div class="edge"></div><div class="box"><div class="name">Nimbra</div><div class="view">View more</div></div></div>
  <div class="provider" style="left:786px"><div class="edge"></div><div class="box"><div class="name">Cirrova</div><div class="view">View more</div></div></div>
</section>

<section class="advice"></section>
<div class="abs kicker" style="left:98px;top:2668px">Knowledgeable</div>
<h2 class="abs h-sec" style="left:98px;top:2700px;font-size:42px">Independent<br>Advice Matters</h2>
<div class="abs copy" style="left:98px;top:2812px;width:380px">
  <p style="margin-bottom:14px">Traditionally, the balance of power lies with your host, who has no interest in you moving to another platform. It may also be that your cloud supplier is a linked to your IT firm, developer or even staff preferences - and in some cases they will specialise in only one of these suppliers.</p>
  <p>It’s time to break free. RMV equips companies, resellers and consultants with the power to choose, to negotiate, to move. We can do this for you.</p>
</div>
<div class="abs" style="left:499px;top:2648px;width:672px;height:479px;border-radius:30px;background:linear-gradient(135deg,#dfe8fb,#b9cdf5)" role="img" aria-label="Isometric illustration of people working beside server racks and a cloud"></div>

<div class="ring"><div class="ring-inner"><span style="font-size:62px;font-weight:600;line-height:64px">20%</span><span style="font-size:40px;font-weight:300">Cheaper</span></div></div>
<div class="abs kicker" style="left:615px;top:3162px">Make your</div>
<h2 class="abs h-sec" style="left:615px;top:3194px">Cloud costs Evaporate</h2>
<p class="abs copy" style="left:615px;top:3257px;width:490px">As cloud costs continue to escalate, and as you suddenly hit new tiers of spend, you may feel helpless in the face of rising costs. However, even taking the cost of moving into account, RMV has estimated the average client will save 20% of spend on their cloud by using us to find the best solution and help you to move there</p>
<a class="btn btn-fill" style="left:617px;top:3418px;width:188px;height:43px">See case studies</a>

<section class="band" style="top:3577px;height:324px">
  <h2 style="margin-top:60px;font-weight:600">Let’s Get Started</h2>
  <p style="font-size:16px;line-height:25px;margin:14px auto 0;width:860px">If you would like to speak to a friendly and helpful member of our team, ask questions, discuss option or to help with anything on your mind, please get in touch.</p>
  <a class="btn btn-line" style="left:403px;top:206px;width:188px;height:45px">Call 01632 960 481</a>
  <a class="btn btn-line" style="left:609px;top:206px;width:185px;height:45px">Send an email</a>
</section>

<h2 class="abs" style="left:0;width:1200px;text-align:center;top:3932px;font-size:40px;font-weight:600">RMV Blog</h2>
<article class="post" style="left:100px"><div class="img" role="img" aria-label="Photo of a hand holding a glowing cloud" style="background:linear-gradient(135deg,#1a2a5a,#6fa6e8)"></div><span class="date">Nov 08, 2022</span><h3>Aliquam sit amet<br>odio cursus</h3><p>Nunc sit amet est sit amet nibh ultricies aliquet ut et justo.</p><a class="btn btn-fill">Read more</a></article>
<article class="post" style="left:354px"><div class="img" role="img" aria-label="Photo of a laptop with glowing network lights" style="background:linear-gradient(135deg,#2b3e6d,#f0a080)"></div><span class="date">Nov 08, 2022</span><h3>Aliquam sit amet<br>odio cursus</h3><p>Nunc sit amet est sit amet nibh ultricies aliquet ut et justo.</p><a class="btn btn-fill">Read more</a></article>
<article class="post" style="left:611px"><div class="img" role="img" aria-label="Photo of a city skyline with a cloud network overlay" style="background:linear-gradient(135deg,#4b6fa3,#1c2f55)"></div><span class="date">Nov 08, 2022</span><h3>Aliquam sit amet<br>odio cursus</h3><p>Nunc sit amet est sit amet nibh ultricies aliquet ut et justo.</p><a class="btn btn-fill">Read more</a></article>
<article class="post" style="left:866px"><div class="img" role="img" aria-label="Photo of a finger touching a glowing cloud diagram" style="background:linear-gradient(135deg,#0f2b3c,#2b6f8c)"></div><span class="date">Nov 08, 2022</span><h3>Aliquam sit amet<br>odio cursus</h3><p>Nunc sit amet est sit amet nibh ultricies aliquet ut et justo.</p><a class="btn btn-fill">Read more</a></article>

<h2 class="abs" style="left:0;width:1200px;text-align:center;top:4508px;font-size:40px;font-weight:400">Trusted <b style="font-weight:600">By</b></h2>
<div class="trust" style="left:89px"><div class="mark"></div><b>CLOUD LOGO</b></div>
<div class="trust" style="left:303px"><div class="mark"></div><b>CLOUD LOGO</b></div>
<div class="trust" style="left:520px"><div class="mark"></div><b>CLOUD LOGO</b></div>
<div class="trust" style="left:745px"><div class="mark"></div><b>CLOUD LOGO</b></div>
<div class="trust" style="left:965px"><div class="mark"></div><b>CLOUD LOGO</b></div>

<footer class="footer">
  <div class="fcol" style="left:98px"><h4>CLOUD SERVICES</h4>Stratobase<br>Nimbra<br>Cirrova<br>Altovia<br>Koreline<br>Tidal Grid<br>Others<br>Private Cloud</div>
  <div class="fcol" style="left:385px"><h4>SERVICES</h4>Cloud Cost Review<br>Migration Planning<br>Migration Execution<br>Security &amp; Compliance<h4 style="margin-top:16px">SOFTWARE</h4>SkyPortal<br>Arc Shift</div>
  <div class="fcol" style="left:655px"><h4>ABOUT RMV</h4>Blog<br>Partners<br>About Us<br>Contact Us
    <div style="margin-top:18px;width:150px;height:62px;border-radius:6px;background:#2e5fd0"></div>
    <div style="margin-top:12px;width:150px;height:40px;border-radius:6px;background:#3a7a52"></div>
  </div>
  <div class="fcol" style="left:925px;line-height:24px"><h4 style="margin-bottom:10px">CONTACT</h4>
    <div style="line-height:33px"><svg width="14" height="14" viewBox="0 0 24 24"><path d="M6 2 L10 6 L8 9 Q10 14 15 16 L18 14 L22 18 L19 22 Q8 21 2 6 Z" fill="#2f8ff2"/></svg>01632 960 481<br>
    <svg width="14" height="12" viewBox="0 0 24 18"><rect width="24" height="18" rx="2" fill="#2f8ff2"/><path d="M1 2 L12 10 L23 2" fill="none" stroke="#1c1b2b" stroke-width="2"/></svg>Email Us<br>
    <svg width="14" height="14"><rect width="14" height="14" rx="2" fill="#2f8ff2"/></svg>Social<br>
    <svg width="14" height="16" viewBox="0 0 24 28"><path d="M12 0 C5 0 1 5 1 11 C1 18 12 28 12 28 C12 28 23 18 23 11 C23 5 19 0 12 0 Z" fill="#2f8ff2"/><circle cx="12" cy="11" r="4" fill="#1c1b2b"/></svg>Alder House</div>
    <div style="padding-left:26px">Mill Road<br>Brookfield<br>BF2 4QA<br>England</div>
  </div>
  <div class="fbottom"><span>(c) RMV Group Limited. All rights reserved</span><nav><span>Sitemap</span><span>Terms of Use</span><span>Privacy Policy</span><span>Contact Us</span></nav></div>
</footer>

</body>
</html>
```